Cat sitting business Web Design Project ***

I have a cat sitting business where I either take care of cats in their home or board them in mine

I need a website which offers my services, my rates, about me, FAQ's, Hours of operation and service areas covered, testimonials, contact info, newsletter sign up, gallery of photos and the ability for me to go in and update when needed.

Coding

Coded - Design and coding required

Number of Pages Required

5+ page

```html
<!DOCTYPE html>
<html lang="en">
<head>
<meta charset="utf-8">
<title>Velvet Paws Cat Sitting</title>
<link href="https://fonts.googleapis.com/css2?family=Poppins:wght@400;500;600;700&family=Great+Vibes&display=swap" rel="stylesheet">
<style>
:root{
  --maroon:#a5545c;
  --maroon-dark:#8e444c;
  --green:#7fbf4d;
  --green-dark:#6aa83c;
  --ink:#2b2b2b;
  --muted:#555;
  --teal-bg:#e7f0ee;
  --mint-bg:#eef5ea;
  --card-grey:#e4e4e6;
  --footer:#1d1d1f;
  --white:#fff;
}
*{box-sizing:border-box;margin:0;padding:0}
html,body{width:1200px;height:5282px;overflow:hidden}
body{font-family:'Poppins',sans-serif;color:var(--ink);background:var(--white);position:relative}
.script{font-family:'Great Vibes',cursive;color:var(--maroon);font-weight:400}
.section{position:absolute;left:0;width:1200px}
.abs{position:absolute}
p{font-size:14px;line-height:24px;color:var(--muted)}
.btn{display:inline-block;padding:11px 24px;border-radius:22px;color:#fff;font-size:14px;font-weight:600;letter-spacing:.3px}
.btn-maroon{background:var(--maroon)}
.btn-green{background:var(--green)}
.photo{border-radius:0}
.heading-green{color:var(--green);font-weight:600;font-size:30px}
.center{text-align:center}

/* top bar */
.topbar{top:0;left:277px;width:923px;height:52px;background:var(--maroon);clip-path:polygon(0 0,100% 0,100% 100%,18px 100%);display:flex;align-items:center;padding-left:60px;gap:44px;color:#fff;font-size:15px}
.topbar .item{display:flex;align-items:center;gap:12px}
.ic{width:30px;height:30px;border:2px solid #fff;border-radius:50%;display:flex;align-items:center;justify-content:center}
.logo{top:12px;left:100px;display:flex;flex-direction:column;align-items:center;gap:6px}
.logo .mark{width:60px;height:60px;border-radius:50%;background:#f3e6e8}
.logo .name{color:var(--maroon);font-weight:600;font-size:17px;text-align:center;line-height:20px}
.nav{top:84px;left:306px;display:flex;gap:34px;font-size:15px}
.nav a{color:var(--ink);text-decoration:none}
.nav a.active{color:var(--green)}
.socials{display:flex;gap:12px}
.soc{width:28px;height:28px;border-radius:50%;background:var(--maroon)}

/* hero */
.hero{top:138px;height:680px;background:linear-gradient(90deg,#f2ece6 0%,#efe4d8 45%,#d8c3aa 70%,#b89a7c 100%);overflow:hidden}
.hero-photo{right:0;top:0;width:560px;height:680px;background:linear-gradient(160deg,#c9a886,#8a6a50 60%,#5f4a3a)}
.hero h1.script{font-size:50px;top:160px;left:105px}
.hero h2{top:222px;left:107px;color:var(--green);font-size:44px;font-weight:700}
.hero p{top:290px;left:111px;width:410px;font-size:15px;color:#333}
.hero .btn{top:386px;left:111px}
.wave{left:0;width:1200px}

/* about */
.about{top:818px;height:597px}
.blob{border-radius:58% 42% 48% 52%/55% 48% 52% 45%}
.about-photo{left:108px;top:2px;width:450px;height:475px;background:linear-gradient(140deg,#c9a46a,#5a4638 55%,#e9e6e2);box-shadow:0 10px 30px rgba(0,0,0,.2)}
.about .script{top:120px;left:634px;font-size:26px}
.about h3{top:156px;left:634px;color:var(--green);font-size:24px;font-weight:600}
.about p{left:634px;width:455px;text-align:justify}
.about .btn{top:390px;left:634px}

/* services */
.services{top:1415px;height:620px;background:var(--teal-bg)}
.services .script{top:80px;width:100%;text-align:center;font-size:24px}
.services h2{top:112px;width:100%;text-align:center}
.card{top:199px;width:232px;height:273px;background:#fff;box-shadow:0 4px 14px rgba(0,0,0,.08);padding:26px 32px}
.card .icon{width:60px;height:60px;border-radius:50%;background:var(--green);display:flex;align-items:center;justify-content:center;margin-bottom:14px}
.card h4{color:var(--green);font-size:17px;font-weight:600;line-height:24px;margin-bottom:12px}
.card p{font-size:12.5px;line-height:19px;text-align:justify}
.card.featured{background:var(--maroon)}
.card.featured h4,.card.featured p{color:#fff}
.card.featured .icon{background:#fff}

/* rates */
.rates{top:2035px;height:627px;background:linear-gradient(90deg,#a5545c,#a04e57 60%,#9b4a53)}
.rates .script{top:132px;left:105px;font-size:26px;color:#fff}
.rates h3{top:172px;left:111px;width:470px;color:#fff;font-size:24px;font-weight:600;line-height:36px}
.rates p{left:111px;width:455px;color:#fbeeee;text-align:justify}
.rates .btn{top:442px;left:111px}
.rates-photo{top:105px;left:638px;width:440px;height:420px;background:radial-gradient(circle at 50% 45%,#b9b2a8,#6f6a63 60%,#3f3b37)}

/* testimonials */
.testimonials{top:2662px;height:610px}
.testimonials .script{top:80px;width:100%;text-align:center;font-size:24px}
.testimonials h2{top:112px;width:100%;text-align:center}
.tcard{width:308px;background:var(--card-grey);text-align:center;padding:56px 30px 20px}
.tcard.featured{background:#fff;box-shadow:0 4px 18px rgba(0,0,0,.15)}
.avatar{position:absolute;left:50%;transform:translateX(-50%);width:64px;height:64px;border-radius:50%;background:linear-gradient(135deg,#6a5a55,#2a2522);border:3px solid #fff}
.tcard h5{color:var(--maroon);font-size:16px;font-weight:600}
.tcard .role{font-size:13px;color:#333;margin-bottom:12px}
.tcard p{font-size:13.5px;line-height:24px;color:#333}
.quote{position:absolute;font-size:34px;color:#999;font-family:Georgia,serif;line-height:1}

/* faq */
.faq{top:3272px;height:603px;background:var(--mint-bg)}
.faq-photo{left:0;top:0;width:507px;height:603px;background:linear-gradient(170deg,#6b5a4f 0%,#8a6a52 40%,#d9a878 70%,#ede3da 100%)}
.faq .script{top:70px;left:562px;font-size:24px}
.faq h2{top:100px;left:562px;font-size:30px}
.q{left:562px;width:525px;background:#fff;border:2px solid #c9e2b3;font-size:14px;font-weight:500;padding:0 20px}
.q .chev{position:absolute;right:16px;top:14px;width:22px;height:22px;border-radius:50%;background:#eef5ea;display:flex;align-items:center;justify-content:center}
.q p{font-size:12.5px;line-height:22px;font-weight:400;margin-top:8px}

/* gallery */
.gallery{top:3875px;height:865px}
.gallery .script{top:110px;width:100%;text-align:center;font-size:24px}
.gallery h2{top:144px;width:100%;text-align:center}
.g{width:232px;height:250px}

/* footer */
.footer{top:4740px;height:542px;background:var(--footer);color:#fff}
.footer .col h6{font-size:15px;font-weight:600;margin-bottom:14px}
.footer .col li{list-style:none;font-size:14px;line-height:31px;color:#e8e8e8}
.footer .flogo{top:150px;left:120px;display:flex;flex-direction:column;align-items:center;gap:10px}
.footer .flogo .mark{width:90px;height:90px;border-radius:50%;background:#3a2f31}
.footer .flogo .name{color:var(--maroon);font-size:26px;font-weight:600;text-align:center;line-height:30px}
.contact-row{display:flex;align-items:flex-start;gap:12px;font-size:15px}
.pin{width:26px;height:26px;border-radius:50%;background:var(--maroon);flex:none;display:flex;align-items:center;justify-content:center}
.email{width:276px;height:40px;border:1px solid #bbb;display:flex;align-items:center;justify-content:space-between;padding:0 12px;font-size:13px}
.copy{bottom:22px;width:100%;text-align:center;font-size:12px;color:#ddd}
</style>
</head>
<body>

<!-- Header -->
<div class="abs logo"><div class="mark"></div><div class="name">Velvet Paws<br>Cat Sitting</div></div>
<div class="abs topbar">
  <div class="item"><span class="ic"><svg width="14" height="14" viewBox="0 0 24 24" fill="#fff"><path d="M6.6 10.8a15 15 0 0 0 6.6 6.6l2.2-2.2c.3-.3.7-.4 1-.2 1.1.4 2.3.6 3.6.6.6 0 1 .4 1 1V20c0 .6-.4 1-1 1A17 17 0 0 1 3 4c0-.6.4-1 1-1h3.5c.6 0 1 .4 1 1 0 1.3.2 2.5.6 3.6.1.3 0 .7-.2 1z"/></svg></span>+1 555 010 2040</div>
  <div class="item"><span class="ic"><svg width="14" height="12" viewBox="0 0 24 18" fill="none" stroke="#fff" stroke-width="2"><rect x="1" y="1" width="22" height="16"/><path d="M1 1l11 9 11-9"/></svg></span>hello@velvetpaws.example</div>
  <div class="item"><span class="ic"><svg width="14" height="14" viewBox="0 0 24 24" fill="none" stroke="#fff" stroke-width="2.4"><circle cx="12" cy="12" r="9"/><path d="M12 7v5l3 2"/></svg></span>Mon - Sun : 10.00 Am To 9 Pm</div>
</div>
<nav class="abs nav">
  <a class="active" href="#">Home</a><a href="#">About Me</a><a href="#">My Rates</a><a href="#">Our Services</a><a href="#">Testimonials</a><a href="#">Contact</a>
</nav>
<div class="abs socials" style="top:78px;left:950px"><span class="soc"></span><span class="soc"></span><span class="soc"></span></div>

<!-- Hero -->
<section class="section hero">
  <div class="abs hero-photo" role="img" aria-label="Woman holding a tabby cat close to her face"></div>
  <h1 class="abs script">Welcome To Velvet Paws</h1>
  <h2 class="abs">Cat Sitting</h2>
  <p class="abs">Lorem ipsum dolor sit amet, consectetur adipiscing elit, sed do eiusmod tempor incididunt ut labore et dolore magna aliqua.</p>
  <span class="abs btn btn-maroon">GET STARTED</span>
  <svg class="abs wave" style="top:555px" width="1200" height="125" viewBox="0 0 1200 125" preserveAspectRatio="none">
    <path d="M0 80 C250 -10 450 40 650 60 C850 80 1000 40 1200 40 L1200 125 L0 125Z" fill="var(--green)"/>
    <path d="M0 100 C250 10 450 58 650 76 C850 96 1000 56 1200 54 L1200 125 L0 125Z" fill="#fff"/>
  </svg>
</section>

<!-- About -->
<section class="section about">
  <div class="abs about-photo blob" role="img" aria-label="Woman cuddling a white cat"></div>
  <div class="abs script">About Me</div>
  <h3 class="abs">Rosalind</h3>
  <p class="abs" style="top:194px">Sed ut perspiciatis unde omnis iste natus error sit voluptatem accusantium doloremque laudantium, totam rem aperiam, eaque ipsa quae ab illo inventore veritatis et quasi architecto beatae vitae dicta sunt explicabo.</p>
  <p class="abs" style="top:298px;text-align:left">Lorem ipsum dolor sit amet, consectetur adipiscing elit, sed do eiusmod tempor incididunt ut labore et dolore magna aliqua. Ut enim ad minim veniam,</p>
  <span class="abs btn btn-maroon">READ MORE</span>
</section>

<!-- Services -->
<section class="section services">
  <div class="abs script">What We're Offering</div>
  <h2 class="abs heading-green">Our Services</h2>
  <div class="abs card" style="left:111px"><div class="icon"><svg width="28" height="28" viewBox="0 0 24 24" fill="#fff"><circle cx="12" cy="14" r="6"/><path d="M6 10 7 4l4 4zM18 10l-1-6-4 4z"/></svg></div><h4>Cat<br>Grooming</h4><p>Sed ut perspiciatis unde omnis iste natus error sit voluptatem accusantium laudantium,</p></div>
  <div class="abs card" style="left:359px"><div class="icon"><svg width="30" height="20" viewBox="0 0 30 20" fill="#fff"><path d="M2 6h26l-3 13H5z"/><rect x="6" y="1" width="18" height="5" rx="2"/></svg></div><h4>Healthy<br>Meals</h4><p>Sed ut perspiciatis unde omnis iste natus error sit voluptatem accusantium laudantium,</p></div>
  <div class="abs card featured" style="left:607px"><div class="icon"><svg width="30" height="30" viewBox="0 0 24 24" fill="var(--maroon)"><circle cx="6" cy="9" r="2.2"/><circle cx="10" cy="5" r="2.2"/><circle cx="14" cy="5" r="2.2"/><circle cx="18" cy="9" r="2.2"/><path d="M12 10c3 0 6 4 6 7 0 2-2 3-6 3s-6-1-6-3c0-3 3-7 6-7z"/></svg></div><h4>Veterinary<br>Care</h4><p>Sed ut perspiciatis unde omnis iste natus error sit voluptatem accusantium laudantium,</p></div>
  <div class="abs card" style="left:855px"><div class="icon"><svg width="28" height="28" viewBox="0 0 24 24" fill="none" stroke="#fff" stroke-width="2"><circle cx="12" cy="12" r="9"/><path d="M4 15c6-1 10-6 12-12M8 20c4-4 9-7 13-8"/></svg></div><h4>Cat<br>Activites</h4><p>Sed ut perspiciatis unde omnis iste natus error sit voluptatem accusantium laudantium,</p></div>
</section>

<!-- Rates -->
<section class="section rates">
  <div class="abs script">My Rates</div>
  <h3 class="abs">Lorem amet, consectetur adipiscing labore et dolore magna aliqua..</h3>
  <p class="abs" style="top:250px">Sed ut perspiciatis unde omnis iste natus error sit voluptatem accusantium doloremque laudantium, totam rem aperiam, eaque ipsa quae ab illo inventore veritatis et quasi architecto beatae vitae dicta sunt explicabo.</p>
  <p class="abs" style="top:352px;text-align:left">Lorem ipsum dolor sit amet, consectetur adipiscing elit, sed do eiusmod tempor incididunt ut labore et dolore magna aliqua. Ut enim ad minim veniam,</p>
  <span class="abs btn btn-green">READ MORE</span>
  <div class="abs rates-photo blob" role="img" aria-label="Close-up of a grey tabby cat"></div>
</section>

<!-- Testimonials -->
<section class="section testimonials">
  <div class="abs script">What Clients Say</div>
  <h2 class="abs heading-green">Testimonials</h2>

  <div class="abs tcard" style="left:111px;top:203px;height:270px">
    <span class="avatar" style="top:-30px"></span>
    <h5>Daniel Brooks</h5><div class="role">Consectetur</div>
    <span class="quote" style="left:12px;top:80px">&ldquo;</span>
    <p>Sed ut perspiciatis unde omnis iste natus error sit voluptatem accusantium doloremque laudantium, totam rem eaque ipsa quae ab</p>
    <span class="quote" style="right:74px;bottom:12px">&rdquo;</span>
  </div>
  <div class="abs tcard featured" style="left:445px;top:203px;height:322px;padding-top:118px">
    <span class="avatar" style="top:28px;width:72px;height:72px"></span>
    <h5>Daniel Brooks</h5><div class="role">Consectetur</div>
    <span class="quote" style="left:12px;top:168px">&ldquo;</span>
    <p>Sed ut perspiciatis unde omnis iste natus error sit voluptatem accusantium doloremque laudantium, totam rem eaque ipsa quae ab</p>
    <span class="quote" style="right:74px;bottom:12px">&rdquo;</span>
  </div>
  <div class="abs tcard" style="left:781px;top:203px;height:270px">
    <span class="avatar" style="top:-30px"></span>
    <h5>Daniel Brooks</h5><div class="role">Consectetur</div>
    <span class="quote" style="left:12px;top:80px">&ldquo;</span>
    <p>Sed ut perspiciatis unde omnis iste natus error sit voluptatem accusantium doloremque laudantium, totam rem eaque ipsa quae ab</p>
    <span class="quote" style="right:74px;bottom:12px">&rdquo;</span>
  </div>
</section>

<!-- FAQ -->
<section class="section faq">
  <div class="abs faq-photo" role="img" aria-label="Ginger cat sleeping while being brushed"></div>
  <div class="abs script">Frequently Asked Questions</div>
  <h2 class="abs heading-green">FREQUENTLY ASKED QUESTIONS</h2>
  <div class="abs q" style="top:155px;height:52px;line-height:48px">Lorem ipsum dolor sit amet, consectetur adipiscing<span class="chev"><svg width="10" height="6" viewBox="0 0 10 6" fill="none" stroke="#555" stroke-width="1.5"><path d="M1 1l4 4 4-4"/></svg></span></div>
  <div class="abs q" style="top:217px;height:160px;padding-top:14px">Lorem ipsum dolor sit amet, consectetur adipiscing ?<span class="chev"><svg width="10" height="6" viewBox="0 0 10 6" fill="none" stroke="#555" stroke-width="1.5"><path d="M1 5l4-4 4 4"/></svg></span>
    <p>Sed ut perspiciatis unde omnis iste natus error sit voluptatem accusantium doloremque laudantium, totam rem aperiam, eaque ipsa quae ab illo inventore veritatis et quasi architecto beatae vitae dicta sunt explicabo.</p></div>
  <div class="abs q" style="top:393px;height:52px;line-height:48px">Lorem ipsum dolor sit amet, consectetur adipiscing<span class="chev"><svg width="10" height="6" viewBox="0 0 10 6" fill="none" stroke="#555" stroke-width="1.5"><path d="M1 1l4 4 4-4"/></svg></span></div>
  <div class="abs q" style="top:463px;height:52px;line-height:48px">Lorem ipsum dolor sit amet, consectetur adipiscing<span class="chev"><svg width="10" height="6" viewBox="0 0 10 6" fill="none" stroke="#555" stroke-width="1.5"><path d="M1 1l4 4 4-4"/></svg></span></div>
</section>

<!-- Gallery -->
<section class="section gallery">
  <div class="abs script">Our Activites</div>
  <h2 class="abs heading-green">OUR GALLERY</h2>
  <div class="abs g" style="left:111px;top:239px;background:linear-gradient(160deg,#e9e6df,#d9b53a 60%,#3a3a3a)" role="img" aria-label="Woman in yellow playing with a black and white cat"></div>
  <div class="abs g" style="left:111px;top:510px;background:linear-gradient(160deg,#5d6b55,#9aa08f 50%,#e6e6e3)" role="img" aria-label="White cat standing on a garden path"></div>
  <div class="abs g" style="left:359px;top:290px;background:linear-gradient(160deg,#d7a0c8,#9a9aa0 50%,#c8a4c0)" role="img" aria-label="Grey tabby cat portrait"></div>
  <div class="abs g" style="left:359px;top:561px;background:linear-gradient(160deg,#6b5443,#c9a889 50%,#2f2a28)" role="img" aria-label="Woman hugging a cat"></div>
  <div class="abs g" style="left:607px;top:239px;background:linear-gradient(160deg,#8aa7b8,#3f5d73 55%,#6d7880)" role="img" aria-label="Grey cat resting on a blue sofa"></div>
  <div class="abs g" style="left:607px;top:510px;background:linear-gradient(160deg,#8a5a3a,#3a2a22 55%,#b38a6a)" role="img" aria-label="Cat eating from a bowl"></div>
  <div class="abs g" style="left:855px;top:290px;background:linear-gradient(160deg,#2a201c,#6a4a34 55%,#1a1614)" role="img" aria-label="Person with a cat in warm window light"></div>
  <div class="abs g" style="left:855px;top:561px;background:linear-gradient(160deg,#eae7e2,#d9b640 60%,#6a4a34)" role="img" aria-label="Girl holding a calico cat"></div>
</section>

<!-- Footer -->
<footer class="section footer">
  <svg class="abs" style="top:-30px;left:0" width="1200" height="90" viewBox="0 0 1200 90" preserveAspectRatio="none">
    <path d="M0 30 C200 0 400 70 650 45 C850 25 1000 60 1200 20 L1200 0 L0 0Z" fill="#fff"/>
    <path d="M0 30 C200 0 400 70 650 45 C850 25 1000 60 1200 20 L1200 34 C1000 74 850 40 650 60 C400 84 200 14 0 44Z" fill="var(--green)"/>
  </svg>
  <div class="abs" style="top:-120px;left:935px;width:130px;height:170px;border-radius:50% 50% 40% 40%;background:linear-gradient(160deg,#9a9a9a,#4a4a4a)" role="img" aria-label="Grey cat peeking over the footer edge"></div>

  <div class="abs flogo"><div class="mark"></div><div class="name">Velvet Paws<br>Cat Sitting</div></div>
  <div class="abs contact-row" style="top:386px;left:120px"><span class="pin"><svg width="10" height="14" viewBox="0 0 10 14" fill="#fff"><path d="M5 0a5 5 0 0 1 5 5c0 4-5 9-5 9S0 9 0 5a5 5 0 0 1 5-5z"/></svg></span><span>0621,Lorem ipsum<br>sit amet,</span></div>
  <div class="abs contact-row" style="top:448px;left:120px"><span class="pin"><svg width="12" height="9" viewBox="0 0 24 18" fill="none" stroke="#fff" stroke-width="2.5"><rect x="1" y="1" width="22" height="16"/><path d="M1 1l11 9 11-9"/></svg></span><span>hello@velvetpaws.example</span></div>
  <div class="abs contact-row" style="top:448px;left:342px"><span class="pin"><svg width="12" height="12" viewBox="0 0 24 24" fill="#fff"><path d="M6.6 10.8a15 15 0 0 0 6.6 6.6l2.2-2.2c.3-.3.7-.4 1-.2 1.1.4 2.3.6 3.6.6.6 0 1 .4 1 1V20c0 .6-.4 1-1 1A17 17 0 0 1 3 4c0-.6.4-1 1-1h3.5c.6 0 1 .4 1 1 0 1.3.2 2.5.6 3.6.1.3 0 .7-.2 1z"/></svg></span><span>+1 555 010 2040</span></div>

  <div class="abs col" style="top:166px;left:355px"><h6>QUICK LINKS</h6><ul><li>Home</li><li>About Me</li><li>My Rates</li><li>Our Services</li><li>Testimonials</li><li>Contact</li></ul></div>
  <div class="abs col" style="top:166px;left:529px"><h6>HOURS OF OPERATION</h6><ul><li>Mon - Fri: 10:00AM - 6:00PM</li><li style="line-height:24px">Sat : 11:30AM - 5:00PM</li><li style="line-height:24px">Sun : 12:00PM - 9:00PM</li></ul></div>
  <div class="abs col" style="top:166px;left:812px"><h6>NEWSLETTER</h6>
    <div class="email"><span>Email</span><svg width="16" height="16" viewBox="0 0 24 24" fill="#fff"><path d="M2 12 22 3l-5 19-5-7z"/></svg></div>
    <div class="socials" style="margin-top:18px"><span class="soc"></span><span class="soc"></span><span class="soc"></span></div>
  </div>
  <div class="abs copy">&copy; 2022 Velvet Paws Cat Sitting | All Rights Reserved</div>
</footer>

</body>
</html>
```